OrvenPharmacy brochure

Need a brochure design for an easy step guid about and how to order from OrvenPharmacy. We would like it very attractive but also clear to read as it is mainly targeting elderly. Attached is 2 alternate logos u can use and the information we would like the brochure to contain

```html
<!DOCTYPE html>
<html lang="en">
<head>
<meta charset="utf-8">
<title>OrvenPharmacy – Rural Medication Service brochure</title>
<link rel="stylesheet" href="https://fonts.googleapis.com/css2?family=Open+Sans:wght@400;600;700&display=swap">
<style>
  :root {
    --stage: #333333;
    --red: #c41e30;
    --red-dark: #9e1524;
    --red-light: #d22a3c;
    --paper: #ffffff;
    --paper-shade: #f1f1f1;
    --silver-1: #c9c9cb;
    --silver-2: #ffffff;
    --ink: #1c1c1c;
    --soft-white: rgba(255,255,255,0.18);
  }
  * { box-sizing: border-box; margin: 0; padding: 0; }
  html, body { width: 1200px; height: 900px; overflow: hidden; }
  body {
    background: var(--stage);
    font-family: "Open Sans", "Segoe UI", sans-serif;
    position: relative;
  }
  .panel {
    position: absolute;
    top: 130px;
    width: 260px;
    height: 640px;
    overflow: hidden;
  }
  .cover-red { left: 60px; background: linear-gradient(100deg, var(--red-dark), var(--red) 45%, var(--red-light)); color: var(--paper); }
  .inside-benefits { left: 340px; background: linear-gradient(90deg, var(--paper-shade), var(--paper) 30%); color: var(--ink); }
  .inside-about { left: 620px; background: var(--paper); color: var(--ink); }
  .cover-silver { left: 900px; background: linear-gradient(90deg, var(--silver-1), var(--silver-2) 25%, var(--silver-2) 75%, var(--silver-1)); }

  /* brand name */
  .brand-name {
    position: absolute; left: 0; right: 0;
    text-align: center;
    font-weight: 600; font-size: 24px; line-height: 1;
  }
  .cover-red .brand-name { top: 205px; }
  .cover-red .cover-title {
    position: absolute; top: 265px; left: 0; right: 0;
    text-align: center; font-size: 21px; font-weight: 400; white-space: nowrap;
  }
  .capsule-pattern {
    position: absolute; left: 0; bottom: 0; width: 100%; height: 300px;
    background: linear-gradient(160deg, transparent 0%, var(--soft-white) 60%, rgba(255,255,255,0.08) 100%);
  }

  /* silver cover */
  .cover-silver .brand-name { top: 140px; color: var(--red); }
  .cover-silver .title-band {
    position: absolute; left: 30px; right: 30px; top: 195px; height: 60px;
    background: var(--red); color: var(--paper);
    display: flex; align-items: center; justify-content: center;
    font-size: 17px; font-weight: 400; white-space: nowrap;
  }
  .cover-silver .red-arch { position: absolute; left: 30px; top: 255px; width: 200px; height: 360px; }

  /* inside panels */
  .band {
    background: linear-gradient(90deg, var(--red-dark), var(--red));
    color: var(--paper); font-weight: 700;
  }
  .band-heading { height: 62px; display: flex; align-items: center; padding: 0 18px; font-size: 19px; }
  .benefit-list { list-style: none; padding: 14px 18px 0; font-size: 12.5px; line-height: 1.35; }
  .benefit-list li { margin-bottom: 9px; }
  .inside-about .band-top { height: 30px; }
  .about-text { padding: 12px 18px; font-size: 15px; line-height: 1.3; }
  .inside-about .band-mid { height: 26px; margin-top: 6px; }
  .sub-heading { color: var(--red-dark); font-weight: 700; font-size: 15px; padding: 14px 18px 0; }
  .inside-about .band-bottom {
    position: absolute; left: 0; right: 0; bottom: 0; height: 90px;
    padding: 16px 18px; font-size: 15px;
  }
</style>
</head>
<body>

  <section class="panel cover-red" aria-label="Front cover">
    <div class="brand-name">OrvenPharmacy</div>
    <h1 class="cover-title">Rural Medication Service</h1>
    <div class="capsule-pattern" role="img" aria-label="Faint capsule and tablet pattern"></div>
  </section>

  <section class="panel inside-benefits" aria-label="Benefits">
    <h2 class="band band-heading">What are the benefits?</h2>
    <ul class="benefit-list">
      <li>Same as City price</li>
      <li>No need to travel</li>
      <li>Delivered by express</li>
      <li>Low delivery costs</li>
      <li>Easy payment methods</li>
      <li>Packed according to your needs</li>
      <li>Sent immediately once we receive your order</li>
      <li>Records kept for easy re-ordering.</li>
      <li>Free Medication Packing</li>
      <li>Add shop items and gifts</li>
      <li>Discounts on bulk purchases.</li>
      <li>Call our service 1300 555 184</li>
    </ul>
  </section>

  <section class="panel inside-about" aria-label="About the service">
    <div class="band band-top"></div>
    <p class="about-text">For over twenty years we have been helping to service rural communities.</p>
    <div class="band band-mid"></div>
    <p class="about-text">We bring medicine to you from local pharmacies, across Australia</p>
    <h3 class="sub-heading">What happens when you order?</h3>
    <p class="about-text">Just fill in the form and we will check prices and what you would like to send before sending.</p>
    <div class="band band-bottom">Call us on:</div>
  </section>

  <section class="panel cover-silver" aria-label="Alternative front cover">
    <div class="brand-name">OrvenPharmacy</div>
    <div class="title-band">Rural Medication Service</div>
    <svg class="red-arch" viewBox="0 0 200 360" aria-hidden="true">
      <defs>
        <linearGradient id="archFill" x1="0" x2="1">
          <stop offset="0" stop-color="#9e1524"/>
          <stop offset="0.5" stop-color="#c41e30"/>
          <stop offset="1" stop-color="#9e1524"/>
        </linearGradient>
      </defs>
      <path d="M0 0 H200 V260 A100 100 0 0 1 0 260 Z" fill="url(#archFill)"/>
    </svg>
  </section>

</body>
</html>
```